Domestic Building Company requires professional webpage

We have an existing webpage that was never completed. We are a growing building company specialising in domestic building, renovations and commercial maintenance. We liaise closely with each of our clients to provide quality service they would be happy to recommend. Our easy approachable staff give our clients the confidence to discuss their needs and changes they may have along the way.
Our main source of new customers have been from recommendations of existing clients.
We would like our webpage to reflect our eye for detail and showcase our previous work.
The colour theme should be the same as the colours of our logo.
We would like the main page to really stand out with a slideshow of our pictures of works we have completed.
We would like the tabs to remain the same - Home, About Us, Our Services, Contact us.
In the Our Services section we would like each sub heading to be a link where viewers can see pictures from previous work we have completed.
Our current web page is www.kestrelbuilding.com.au

```html
<!DOCTYPE html>
<html lang="en">
<head>
<meta charset="utf-8">
<title>Kestrel Building Services</title>
<link href="https://fonts.googleapis.com/css2?family=Lato:wght@300;400;700&display=swap" rel="stylesheet">
<style>
:root{
  --black:#000;
  --green:#8dc63f;
  --blue:#1565b5;
  --paper:#f7f6f2;
  --text:#6b6b6b;
  --muted:#8a8a8a;
  --white:#fff;
}
*{margin:0;padding:0;box-sizing:border-box}
html,body{width:1186px;height:1200px;overflow:hidden}
body{background:var(--paper);font-family:'Lato',sans-serif;position:relative;color:var(--text)}
.abs{position:absolute}

/* header */
.site-header{position:absolute;left:0;top:0;width:1186px;height:125px;background:var(--black);border-bottom:3px solid var(--blue)}
.header-frame{position:absolute;left:30px;top:14px;width:1126px;height:91px;border:1px solid #5a5a5a;border-top:none}
.frame-top-l{position:absolute;left:30px;top:14px;width:56px;height:1px;background:#5a5a5a}
.frame-top-m{position:absolute;left:356px;top:14px;width:604px;height:1px;background:#5a5a5a}
.frame-top-r{position:absolute;left:1100px;top:14px;width:56px;height:1px;background:#5a5a5a}
.frame-gap{position:absolute;left:327px;top:100px;width:490px;height:8px;background:var(--black)}
.utility-nav{position:absolute;left:89px;top:10px;display:flex;gap:16px;font-size:7.5px;color:#ddd;letter-spacing:.1px;background:var(--black);padding-right:4px}
.phone{position:absolute;left:972px;top:6px;display:flex;align-items:center;gap:8px;color:var(--green);font-weight:700;font-size:14px;background:var(--black);padding:0 8px}
.brand{position:absolute;left:87px;top:36px;display:flex;align-items:flex-end;gap:8px;color:var(--green)}
.brand-name{font-weight:300;font-size:36px;line-height:30px}
.brand-sub{display:block;font-size:8px;letter-spacing:2.4px;line-height:12px}
.brand-mark{width:40px;height:40px;background:var(--green);margin-bottom:2px}
.main-nav{position:absolute;left:343px;top:87px;display:flex;gap:12px}
.main-nav a{display:block;width:107px;height:30px;border:1px solid #cfcfcf;border-radius:2px;color:var(--white);text-decoration:none;font-size:15px;text-align:center;line-height:28px;background:var(--black)}
.main-nav a.active{color:var(--green)}

/* slider */
.slide{position:absolute;border:1px solid var(--blue);padding:3px;background:var(--white)}
.slide .photo{width:100%;height:100%}
.slide.center{border-color:#b7d37a;padding:5px}
.reflect{position:absolute;background:linear-gradient(#dcdcd8,rgba(247,246,242,0));opacity:.7}
.arrow{position:absolute;top:307px;width:44px;height:44px}
.dots{position:absolute;left:459px;top:512px;display:flex;gap:7px}
.dots span{width:13px;height:13px;border-radius:50%;background:var(--green)}
.dots span.on{background:var(--blue)}

/* intro */
.intro{position:absolute;left:88px;top:582px;width:1010px;font-size:12.6px;line-height:15.5px;font-weight:300;color:var(--text)}
.intro strong{font-size:15px;font-weight:400;color:#666}
.divider{position:absolute;left:87px;top:689px;width:1012px;height:2px;border-top:1px solid var(--blue);border-bottom:1px solid var(--green)}

/* services */
.section-title{position:absolute;left:88px;top:726px;font-size:21px;font-weight:400;color:var(--blue)}
.service{position:absolute;top:776px;width:140px}
.service h3{font-size:10.5px;font-weight:700;color:var(--blue);height:27px}
.service .thumb{width:139px;height:102px;border:2px solid #c9c9c9}
.service p{margin-top:16px;font-size:10.4px;line-height:12.4px;font-weight:300;color:#555;width:134px}

/* footer */
.site-footer{position:absolute;left:0;top:1025px;width:1186px;height:175px;background:var(--black)}
.footer-nav{position:absolute;left:88px;top:13px;display:flex;gap:31px;font-size:11.5px}
.footer-nav a{color:var(--white);text-decoration:none}
.footer-nav a.active{color:var(--green)}
.footer-rule{position:absolute;left:0;top:38px;width:1186px;height:1px;background:#2a2a2a}
.badge{position:absolute;left:87px;top:54px;width:158px;height:73px;background:var(--white);border:2px solid var(--blue)}
.follow{position:absolute;left:0;width:1186px;top:57px;text-align:center;font-size:13.5px;color:#8a8a8a;font-weight:400}
.social{position:absolute;left:467px;top:91px;display:flex;gap:24px}
.social span{width:31px;height:31px;border-radius:50%;background:linear-gradient(#e0e0e0,#9e9e9e)}
.footer-brand{position:absolute;left:911px;top:63px;display:flex;align-items:flex-end;gap:8px;color:#8a8a8a}
.footer-brand .brand-mark{background:#6a6a6a}
.copy-rule{position:absolute;left:0;top:141px;width:1186px;height:1px;background:#2a2a2a}
.copyright{position:absolute;left:88px;top:151px;font-size:10px;color:#8a8a8a}
</style>
</head>
<body>

<header class="site-header">
  <div class="header-frame"></div>
  <div class="frame-top-l"></div><div class="frame-top-m"></div><div class="frame-top-r"></div>
  <div class="frame-gap"></div>
  <nav class="utility-nav"><span>ALL BUILDING</span><span>TRACK MY BUILDING</span><span>CONTACT US</span><span>NEWS</span></nav>
  <div class="phone">
    <svg width="14" height="18" viewBox="0 0 14 18"><path d="M3 1 L6 5 L4.5 7 Q6 11 9 13.5 L11 12 L13 16 L11 17.5 Q4 15 1.5 4 Z" fill="none" stroke="#ddd" stroke-width="1.2"/></svg>
    0800-555-019
  </div>
  <div class="brand">
    <div><span class="brand-name">kestrel</span><span class="brand-sub">BUILDING SERVICES</span></div>
    <span class="brand-mark"></span>
  </div>
  <nav class="main-nav">
    <a class="active">Home</a><a>About Us</a><a>Our Services</a><a>Contact us</a>
  </nav>
</header>

<!-- slideshow -->
<div class="reflect" style="left:229px;top:400px;width:86px;height:38px"></div>
<div class="reflect" style="left:862px;top:400px;width:86px;height:38px"></div>
<div class="reflect" style="left:314px;top:430px;width:94px;height:40px"></div>
<div class="reflect" style="left:767px;top:430px;width:94px;height:40px"></div>
<div class="reflect" style="left:408px;top:455px;width:356px;height:50px"></div>

<div class="slide" style="left:228px;top:264px;width:90px;height:132px">
  <div class="photo" role="img" aria-label="Timber deck with garden trees" style="background:linear-gradient(#7aa04e,#b9a878 60%,#c7b48d)"></div>
</div>
<div class="slide" style="left:866px;top:264px;width:82px;height:132px">
  <div class="photo" role="img" aria-label="Timber deck with garden trees" style="background:linear-gradient(#7aa04e,#b9a878 60%,#c7b48d)"></div>
</div>
<div class="slide" style="left:312px;top:234px;width:100px;height:190px">
  <div class="photo" role="img" aria-label="Renovated interior room" style="background:linear-gradient(135deg,#3a2a20,#8a7a68 50%,#2a1d15)"></div>
</div>
<div class="slide" style="left:762px;top:234px;width:101px;height:190px">
  <div class="photo" role="img" aria-label="Renovated interior room" style="background:linear-gradient(225deg,#3a2a20,#8a7a68 50%,#2a1d15)"></div>
</div>
<div class="slide center" style="left:405px;top:203px;width:362px;height:245px">
  <div class="photo" role="img" aria-label="Renovated open-plan living room with timber floor" style="background:linear-gradient(#5a4a3e,#a89a88 45%,#6e6258 75%,#b8ada0)"></div>
</div>

<svg class="arrow" style="left:89px" viewBox="0 0 44 44"><circle cx="22" cy="22" r="20.5" fill="none" stroke="#1565b5" stroke-width="2"/><path d="M25 13 L16 22 L25 31" fill="none" stroke="#1565b5" stroke-width="1"/></svg>
<svg class="arrow" style="left:1054px" viewBox="0 0 44 44"><circle cx="22" cy="22" r="20.5" fill="none" stroke="#1565b5" stroke-width="2"/><path d="M19 13 L28 22 L19 31" fill="none" stroke="#1565b5" stroke-width="1"/></svg>

<div class="dots"><span class="on"></span><span></span><span></span><span></span><span></span><span></span><span></span><span></span><span></span><span></span><span></span><span></span></div>

<p class="intro"><strong>Kestrel Building Services Pty Ltd</strong> is a construction and renovation company that is based in the Illawarra area.&nbsp; We specialise in all areas of residential and commercial building works and aim to deliver the highest quality performance at an affordable price. We ensure our workers have undergone the qualifications and training to provide the workmanship, efficiency and reliability our clients expect. We actively engage our client from the initial greeting to the finished product, we achieve this by ensuring the clients needs remain our first priority when delivering a high quality service and product.</p>

<div class="divider"></div>

<h2 class="section-title">OUR SERVICES</h2>

<div class="service" style="left:87px"><h3>PERGOLAS</h3><div class="thumb" role="img" aria-label="Timber pergola over paved patio" style="background:linear-gradient(#c9cdd2,#a0643a 55%,#8a8a86)"></div><p>Create a functional open air outdoor room great for entertaining, improve the appearance of home and add extra space.</p></div>
<div class="service" style="left:231px"><h3>DECKS</h3><div class="thumb" role="img" aria-label="Curved hardwood deck" style="background:linear-gradient(#4f6a3a,#b87a3a 60%,#8a5526)"></div><p>We create and design various shape and sized hardwood decks to cater for all styles of homes.</p></div>
<div class="service" style="left:375px"><h3>BATHROOMS</h3><div class="thumb" role="img" aria-label="Modern bathroom with timber finish" style="background:linear-gradient(135deg,#6b4a2a,#d8b070 50%,#4d3520)"></div><p>Update and modernise existing or new bathrooms to suit your style and needs.</p></div>
<div class="service" style="left:520px"><h3>COMMERCIAL FIT-OUT</h3><div class="thumb" role="img" aria-label="Refurbished commercial office space" style="background:linear-gradient(#3d3630,#9a9790 55%,#5e6a6a)"></div><p>Office or shop refurbishment to create a practical and modern design to cater for your business.</p></div>
<div class="service" style="left:666px"><h3>TIMBER FLOORING</h3><div class="thumb" role="img" aria-label="Kitchen with solid timber floor" style="background:linear-gradient(#f2f2f0,#e6e4e0 45%,#c97d3a 70%,#b56a2a)"></div><p>We install all aspects of timber flooring ranging from floating floors through to solid hardwood flooring for a modern look.</p></div>
<div class="service" style="left:811px"><h3>ALUMINIUM / TIMBER</h3><div class="thumb" role="img" aria-label="Timber slat gate and fence" style="background:linear-gradient(90deg,#a85a32,#c07048 50%,#8a6a50)"></div><p>We install a variety of timber or aluminium windows and doors including single doors, bifold doors.</p></div>
<div class="service" style="left:957px"><h3>BUILDING MAINTENANCE</h3><div class="thumb" role="img" aria-label="Tradesmen working with a power saw" style="background:linear-gradient(135deg,#c98a3a,#5a3a22 50%,#d8a050)"></div><p>We provide a home repair service for all internal and external problems, no job too small.</p></div>

<footer class="site-footer">
  <nav class="footer-nav"><a class="active">Home</a><a>About Us</a><a>Our Services</a><a>Contact us</a></nav>
  <div class="footer-rule"></div>
  <div class="badge" role="img" aria-label="Industry association membership badge"></div>
  <div class="follow">FOLLOW US</div>
  <div class="social"><span></span><span></span><span></span><span></span><span></span></div>
  <div class="footer-brand">
    <div><span class="brand-name">kestrel</span><span class="brand-sub">BUILDING SERVICES</span></div>
    <span class="brand-mark"></span>
  </div>
  <div class="copy-rule"></div>
  <p class="copyright">Copyright 2014 Kestrel Building Services Pty Ltd | ABN: 40 118 274 903 | Lic: 204815K</p>
</footer>

</body>
</html>
```